Machining Business Order Thank You Insert

I am looking for a business style card to include with orders that I ship. The card needs to thank the recipient for their order, and encourage them to leave a review. The card should include my business name and contact information and have an area to hand write a message.

I mainly sale on Crafvine and my own website. We are a machining an manufacturing business that are in the sale of mostly metal machined and 3d printed plastic products.

The front of the card should include the following:
Logo: (attached)
Snapgrid: https://www.instagram.com/quillforge/
Friendwall: https://www.facebook.com/QuillForge
Website: https://www.quillforge-example.com/

The back of the card needs an area to write a message

Industry/Entity Type

3D Printing, Machining, Crafvine

Contact Information for Business Card

Black or white front, white back to write a personal message

Font styles to use
Sans Serif

Colors

Designer to choose colors to be used in the design.

Requirements
Must have
• Encourage a review, social media info

```html
<!DOCTYPE html>
<html lang="en">
<head>
<meta charset="utf-8">
<title>QuillForge Thank You Inserts</title>
<link rel="stylesheet" href="https://fonts.googleapis.com/css2?family=Questrial&family=Jost:wght@600&family=Roboto:wght@300&display=swap">
<style>
  :root {
    --backdrop: #4b4b4d;
    --ink-black: #000000;
    --paper: #ffffff;
    --accent: #ef5a2c;
    --grey-text: #5a5a5a;
    --rule: #8a8a8a;
    --label: #ffffff;
    --photo-light: #cfcfcf;
    --photo-mid: #8c8c8c;
    --photo-dark: #2a2a2a;
  }
  * { box-sizing: border-box; margin: 0; padding: 0; }
  html, body { width: 1200px; height: 1194px; overflow: hidden; }
  body { background: var(--backdrop); position: relative; font-family: "Questrial", sans-serif; }

  .size-label {
    position: absolute; transform: translate(-50%, -50%);
    font-family: "Roboto", sans-serif; font-weight: 300;
    font-size: 48px; color: var(--label); line-height: 1;
  }

  .card { position: absolute; overflow: hidden; box-shadow: 3px 4px 8px rgba(0,0,0,.45); }
  .card--front { background: var(--ink-black); }
  .card--back { background: var(--paper); }
  .card--large { width: 414px; height: 276px; font-size: 10px; }
  .card--small { width: 345px; height: 241px; font-size: 8.4px; }
  .card--tall { width: 276px; height: 414px; font-size: 10px; }

  .photo {
    position: absolute; inset: 0;
    background: radial-gradient(circle at 65% 40%, var(--photo-light), var(--photo-mid) 45%, var(--photo-dark) 100%);
  }
  .photo--side { clip-path: polygon(53% 0, 100% 0, 100% 100%, 61% 100%); }
  .photo--top { clip-path: polygon(0 0, 100% 0, 100% 47%, 0 54.5%); }

  .at { position: absolute; transform: translate(-50%, -50%); white-space: nowrap; text-align: center; }

  .brand {
    display: flex; align-items: center; gap: .6em;
    font-size: 1.05em; letter-spacing: .35em; color: var(--accent);
  }
  .brand__mark { width: .9em; height: .9em; background: var(--accent); }

  .link { font-size: .82em; letter-spacing: .1em; color: var(--paper); }
  .link__label { color: var(--accent); }

  .headline {
    font-family: "Jost", sans-serif; font-weight: 600;
    font-size: 3.4em; color: var(--accent); line-height: 1; letter-spacing: .01em;
  }
  .subline { font-size: 1.85em; color: var(--grey-text); line-height: 1; }
  .card--tall .headline { font-size: 3.4em; }
  .card--tall .subline { font-size: 1.85em; }

  .rule { position: absolute; height: 0; border-top: 1px solid var(--rule); }

  .note { font-size: .9em; letter-spacing: .08em; color: var(--grey-text); line-height: 1.55; }
  .note__link { color: var(--accent); }
  .card--tall .note { font-size: .85em; line-height: 2.1; }
  .stars { font-size: 1.9em; letter-spacing: .25em; color: var(--accent); line-height: 1; padding-left: .25em; }
</style>
</head>
<body>

  <span class="size-label" style="left:323px;top:50px">6"</span>
  <span class="size-label" style="left:81px;top:214px">4"</span>
  <span class="size-label" style="left:890px;top:87px">5"</span>
  <span class="size-label" style="left:1112px;top:239px">3.5"</span>
  <span class="size-label" style="left:440px;top:708px">4"</span>
  <span class="size-label" style="left:264px;top:941px">6"</span>

  <!-- 6 x 4 front -->
  <section class="card card--front card--large" style="left:114px;top:82px">
    <div class="photo photo--side" role="img" aria-label="Black and white close-up of a machined metal part"></div>
    <div class="at brand" style="left:28%;top:50%"><span class="brand__mark"></span>QUILLFORGE</div>
    <p class="at link" style="left:28%;top:61%"><span class="link__label">Snapgrid:</span> www.snapgrid-example.com/quillforge</p>
    <p class="at link" style="left:28%;top:67.5%"><span class="link__label">Friendwall:</span> www.friendwall-example.com/QuillForge</p>
    <p class="at link" style="left:28%;top:74%"><span class="link__label">Website:</span> www.quillforge-example.com</p>
  </section>

  <!-- 6 x 4 back -->
  <section class="card card--back card--large" style="left:114px;top:387px">
    <div class="at brand" style="left:50%;top:24%"><span class="brand__mark"></span>QUILLFORGE</div>
    <h1 class="at headline" style="left:50%;top:35%">THANK YOU</h1>
    <p class="at subline" style="left:50%;top:43.5%">For your purchase!</p>
    <div class="rule" style="left:26%;right:26%;top:51%"></div>
    <div class="rule" style="left:18%;right:18%;top:56%"></div>
    <div class="rule" style="left:18%;right:18%;top:61%"></div>
    <p class="at note" style="left:50%;top:71%">If you are satisfied with your purchase. Please take a few moments to leave<br>us a feedback review for us at <span class="note__link">www.crafvine.com/shop/QuillForge</span></p>
    <p class="at stars" style="left:50%;top:80%">★★★★★</p>
    <p class="at note" style="left:50%;top:89%">If there is a problem with your order please contact us<br>and let us resolve it for you before leaving feedback</p>
  </section>

  <!-- 5 x 3.5 front -->
  <section class="card card--front card--small" style="left:708px;top:122px">
    <div class="photo photo--side" role="img" aria-label="Black and white close-up of a machined metal part"></div>
    <div class="at brand" style="left:30%;top:49%"><span class="brand__mark"></span>QUILLFORGE</div>
    <p class="at link" style="left:30%;top:61%"><span class="link__label">Snapgrid:</span> www.snapgrid-example.com/quillforge</p>
    <p class="at link" style="left:30%;top:67.5%"><span class="link__label">Friendwall:</span> www.friendwall-example.com/QuillForge</p>
    <p class="at link" style="left:30%;top:74%"><span class="link__label">Website:</span> www.quillforge-example.com</p>
  </section>

  <!-- 5 x 3.5 back -->
  <section class="card card--back card--small" style="left:708px;top:394px">
    <div class="at brand" style="left:50%;top:25%"><span class="brand__mark"></span>QUILLFORGE</div>
    <h2 class="at headline" style="left:50%;top:36%">THANK YOU</h2>
    <p class="at subline" style="left:50%;top:44.5%">For your purchase!</p>
    <div class="rule" style="left:26%;right:26%;top:51%"></div>
    <div class="rule" style="left:18%;right:18%;top:56%"></div>
    <div class="rule" style="left:18%;right:18%;top:61%"></div>
    <p class="at note" style="left:50%;top:70%">If you are satisfied with your purchase. Please take a few moments to leave<br>us a feedback review for us at <span class="note__link">www.crafvine.com/shop/QuillForge</span></p>
    <p class="at stars" style="left:50%;top:78%">★★★★★</p>
    <p class="at note" style="left:50%;top:87%">If there is a problem with your order please contact us<br>and let us resolve it for you before leaving feedback</p>
  </section>

  <!-- 4 x 6 front -->
  <section class="card card--front card--tall" style="left:303px;top:740px">
    <div class="photo photo--top" role="img" aria-label="Black and white close-up of a machined metal part"></div>
    <div class="at brand" style="left:50%;top:75%"><span class="brand__mark"></span>QUILLFORGE</div>
    <p class="at link" style="left:50%;top:83%"><span class="link__label">Snapgrid:</span> www.snapgrid-example.com/quillforge</p>
    <p class="at link" style="left:50%;top:87%"><span class="link__label">Friendwall:</span> www.friendwall-example.com/QuillForge</p>
    <p class="at link" style="left:50%;top:91%"><span class="link__label">Website:</span> www.quillforge-example.com</p>
  </section>

  <!-- 4 x 6 back -->
  <section class="card card--back card--tall" style="left:632px;top:740px">
    <div class="at brand" style="left:50%;top:25%"><span class="brand__mark"></span>QUILLFORGE</div>
    <h2 class="at headline" style="left:50%;top:35%">THANK YOU</h2>
    <p class="at subline" style="left:50%;top:40.5%">For your purchase!</p>
    <div class="rule" style="left:17%;right:17%;top:49%"></div>
    <div class="rule" style="left:6%;right:6%;top:52%"></div>
    <div class="rule" style="left:6%;right:6%;top:55%"></div>
    <div class="rule" style="left:6%;right:6%;top:58%"></div>
    <div class="rule" style="left:6%;right:6%;top:61%"></div>
    <p class="at note" style="left:50%;top:71.5%">If you are satisfied with your purchase. Please take a few<br>moments to leave us a feedback review for us at<br><span class="note__link">www.crafvine.com/shop/QuillForge</span></p>
    <p class="at stars" style="left:50%;top:80.5%">★★★★★</p>
    <p class="at note" style="left:50%;top:89%">If there is a problem with your order please contact us<br>and let us resolve it for you before leaving feedback</p>
  </section>

</body>
</html>
```